13 Tovi - new website design project

Our company Tovi Electrical is developing a new lead generation website focused on Electrical, LED Lighting and Solar Power. We need a high converting website.

Example of our current website is www.tovielectrical.com.au You can take content from this website for this new design. Our colours are red, black and white. For our new website we would like to promote Tovi, Bright Days Ahead. Please listen to the jingle.

The below link is the company jingle that we have developed.
http://www.tunecraftstudio.com.au/tov-tc-v1/

The key for this brief is to generate leads for Electrical, LED Lighting (for commercial) and Solar Power & Storage.

Target Market(s)

Business owners in Melbourne Victoria

Number of Pages Required

4 page

Colors
ec1f27
ffffff

Requirements
Must have
• This page must be clean, be in line with company branding and a high converting lead website.

```html
<!DOCTYPE html>
<html lang="en">
<head>
<meta charset="utf-8">
<title>Tovi Story – Tovi Electrical</title>
<link rel="stylesheet" href="https://fonts.googleapis.com/css2?family=Lato:wght@400;700;900&family=Open+Sans:ital,wght@0,400;0,600;0,700;1,400;1,600&display=swap">
<style>
:root{
  --red:#ec1f27;
  --ink:#222222;
  --text:#555555;
  --muted:#888888;
  --line:#dddddd;
  --dark:#2e3138;
  --grey-band:#e4e4e4;
  --white:#ffffff;
}
*{box-sizing:border-box;margin:0;padding:0}
html,body{width:1200px;height:2667px;overflow:hidden;background:var(--white)}
body{position:relative;font-family:"Open Sans",Arial,sans-serif;color:var(--text)}
.abs{position:absolute}

/* header */
.top-strip{left:0;top:0;width:1200px;height:5px;background:linear-gradient(90deg,var(--red) 0 52%,var(--dark) 52% 100%)}
.brand{left:98px;top:16px;display:flex;align-items:center;gap:12px;font-family:"Lato",sans-serif;font-weight:900;font-size:44px;color:var(--red);letter-spacing:1px}
.brand-dot{width:22px;height:22px;border-radius:50%;background:var(--red)}
.quick-contact{top:14px;display:flex;align-items:center;gap:10px;font-size:15px;color:var(--ink);font-weight:600}
.icon-ring{width:30px;height:30px;border-radius:50%;border:1px solid var(--line);display:flex;align-items:center;justify-content:center}
.main-nav{right:97px;top:62px;display:flex;gap:38px;font-family:"Lato",sans-serif;font-weight:700;font-size:15px;color:var(--ink);align-items:center}
.main-nav .active{color:var(--red)}

/* hero */
.hero{left:0;top:94px;width:1200px;height:301px;background:linear-gradient(180deg,#4a3a28 0%,#b88a3e 30%,#6b6a55 60%,#3d4a2a 100%)}
.hero-title{left:0;top:200px;width:1200px;text-align:center;font-family:"Lato",sans-serif;font-weight:700;font-size:62px;color:var(--white)}
.hero-dots{left:533px;top:354px;display:flex;gap:6px}
.hero-dots span{width:30px;height:4px;background:rgba(255,255,255,.8)}
.hero-dots span.on{background:var(--red)}

/* breadcrumb */
.breadcrumb{left:98px;top:428px;font-family:"Lato",sans-serif;font-weight:700;font-size:15px;color:var(--ink)}
.breadcrumb b{color:var(--red)}
.rule{height:1px;background:var(--line);left:98px;width:1004px}

/* profile */
.portrait-frame{left:98px;top:537px;width:375px;height:453px;border:1px solid var(--line);padding:6px;background:var(--white)}
.portrait{width:100%;height:100%;background:linear-gradient(180deg,#ececec,#d6d6d6)}
.founder-name{left:526px;top:530px;font-family:"Lato",sans-serif;font-weight:900;font-size:28px;color:var(--ink)}
.founder-role{left:526px;top:578px;font-size:17px;color:var(--red)}
.founder-bio{left:526px;top:622px;width:576px;font-size:12.3px;line-height:24px;color:var(--text)}
.founder-bio p+p{margin-top:24px}
.founder-sign{left:526px;top:955px;font-family:"Lato",sans-serif;font-style:italic;font-size:22px;color:#666}

/* promise */
.section-title{left:0;width:1200px;text-align:center;font-family:"Lato",sans-serif;font-weight:900;font-size:25px;color:var(--ink)}
.promise{top:1177px;width:320px;text-align:center}
.promise-ring{width:157px;height:157px;border-radius:50%;border:1px solid #cfcfcf;margin:0 auto;display:flex;align-items:center;justify-content:center}
.promise h3{margin-top:30px;font-family:"Open Sans",sans-serif;font-weight:600;font-size:21px;color:var(--ink)}
.promise p{margin-top:14px;font-size:12.3px;line-height:24px;color:var(--text)}

/* services band */
.services{left:0;top:1538px;width:1200px;height:382px;background:linear-gradient(120deg,#38404e 0%,#2a3344 45%,#3a4660 70%,#4b5a3c 100%)}
.services-title{left:100px;top:1590px;font-family:"Open Sans",sans-serif;font-weight:700;font-size:25px;color:var(--white)}
.service-col{top:1661px;list-style:none;font-size:14px;font-weight:600;color:var(--white)}
.service-col li{height:29.2px;display:flex;align-items:center;gap:9px}
.tick{width:15px;height:15px;border-radius:50%;background:var(--white);display:flex;align-items:center;justify-content:center;flex:none}

/* testimonial */
.testimonial{left:0;top:1920px;width:1200px;height:267px;background:var(--grey-band)}
.client-frame{left:98px;top:1968px;width:275px;height:183px;border:1px solid #cccccc;background:var(--white);padding:4px}
.client-photo{width:100%;height:100%;background:linear-gradient(180deg,#f2d300 0 34%,#8d8f93 34% 100%)}
.quote-bar{left:410px;top:1996px;width:1px;height:130px;background:#bbbbbb}
.quote{left:443px;top:2006px;width:680px;font-style:italic;font-size:13.5px;line-height:30px;color:var(--text)}
.quote-by{left:443px;top:2082px;font-size:16px;font-weight:600;color:var(--red)}
.quote-by i{font-weight:400}
.slider-arrow{top:2040px}

/* contact */
.get-in-touch{left:98px;top:2314px;font-weight:600;font-size:19px;color:var(--ink)}
.field{height:32px;border:1px solid #cccccc;font-size:12px;color:#777;padding:8px 12px;background:var(--white)}
.submit{left:588px;top:2517px;width:116px;height:40px;background:linear-gradient(135deg,var(--red) 0 80%,#9e1016 80% 100%);color:var(--white);font-weight:700;font-size:15px;display:flex;align-items:center;justify-content:center;padding-right:14px;letter-spacing:1px}
.info-title{left:782px;top:2314px;font-weight:600;font-size:19px;color:var(--ink)}
.info-row{left:782px;display:flex;gap:25px;font-size:13px;line-height:23px;color:var(--text)}
.info-ring{width:38px;height:38px;border-radius:50%;border:1px solid var(--line);display:flex;align-items:center;justify-content:center;flex:none}

/* footer */
.footer-dark{left:0;top:2603px;width:1200px;height:64px;background:var(--dark)}
.footer-red{left:0;top:2603px;width:660px;height:64px;background:var(--red);clip-path:polygon(0 0,615px 0,660px 64px,0 64px)}
.copyright{left:98px;top:2626px;font-size:12px;color:var(--white)}
.socials{left:977px;top:2618px;display:flex;gap:7px}
.socials span{width:27px;height:27px;border-radius:50%;border:1px solid rgba(255,255,255,.8)}
</style>
</head>
<body>

<header>
  <div class="abs top-strip"></div>
  <div class="abs brand"><span class="brand-dot"></span>Tovi</div>
  <div class="abs quick-contact" style="left:671px">
    <span class="icon-ring"><svg width="14" height="14" viewBox="0 0 24 24"><path fill="#ec1f27" d="M6.6 10.8a15 15 0 0 0 6.6 6.6l2.2-2.2c.3-.3.7-.4 1-.2 1.1.4 2.3.6 3.6.6.6 0 1 .4 1 1V20c0 .6-.4 1-1 1A17 17 0 0 1 3 4c0-.6.4-1 1-1h3.5c.6 0 1 .4 1 1 0 1.3.2 2.5.6 3.6.1.3 0 .7-.2 1z"/></svg></span>139471TOVI
  </div>
  <div class="abs quick-contact" style="left:845px">
    <span class="icon-ring"><svg width="14" height="14" viewBox="0 0 24 24"><path fill="#ec1f27" d="M3 5h18v14H3z"/><path fill="none" stroke="#fff" stroke-width="2" d="M3 6l9 7 9-7"/></svg></span>service@tovielectrical.com.au
  </div>
  <nav class="abs main-nav">
    <span>HOME</span><span class="active">TOVI STORY</span><span>SERVICES</span><span>OUR WORK</span><span>SOLAR POWER</span><span>CONTACT US</span>
    <svg width="15" height="15" viewBox="0 0 24 24"><circle cx="10" cy="10" r="7" fill="none" stroke="#222" stroke-width="3"/><path d="M15 15l6 6" stroke="#222" stroke-width="3"/></svg>
  </nav>
</header>

<section>
  <div class="abs hero" role="img" aria-label="Solar panel fields and wind turbines under a golden sunset sky"></div>
  <h1 class="abs hero-title">Tovi Story</h1>
  <div class="abs hero-dots"><span class="on"></span><span></span><span></span><span></span></div>
</section>

<div class="abs breadcrumb">HOME &nbsp;&gt;&gt;&nbsp; <b>TOVI STORY</b></div>
<div class="abs rule" style="top:471px"></div>

<section>
  <div class="abs portrait-frame"><div class="portrait" role="img" aria-label="Portrait of the managing director in a dark suit"></div></div>
  <h2 class="abs founder-name">MARCUS DELANE</h2>
  <div class="abs founder-role">Tovi Electrical. REC #27461 &nbsp;|&nbsp; Managing Director &amp; Founder</div>
  <div class="abs founder-bio">
    <p>Tovi Electrical is an expert Electrical Company providing services to all Residential and Commercial customers. With over 10 years of experience, Tovi Electrical has developed a highly-experienced team of professionals that ensure all our customer expectations are exceeded. Our team comprise of over 70 staff of Designers, Consultants, Electricians who provide expert advice and quality of installation at an affordable price.</p>
    <p>Today, Tovi Electrical have installed over 200,000 LED Lights, 50,000 Solar Panels and have created greater energy independence from the grid while providing great return on investments. Tovi Electrical has grown to become one of Australia's largest fully integrated Electrical &amp; Energy Solutions providers. As a result, we are able to offer our customers the most competitive prices for LED Lighting Upgrades and Solar Power solutions. Quality, Reliability and Customer First – these are the key foundations that we offer our customers. All work is covered by a 5 year workmanship warranty and a minimum 1 year warranty on all products.</p>
  </div>
  <div class="abs founder-sign">Marcus Delane</div>
</section>

<div class="abs rule" style="top:1060px"></div>

<section>
  <h2 class="abs section-title" style="top:1108px">OUR PROMISE</h2>
  <div class="abs promise" style="left:94px">
    <div class="promise-ring"><svg width="66" height="66" viewBox="0 0 24 24"><rect x="2" y="10" width="5" height="11" rx="1" fill="#ec1f27"/><path fill="#ec1f27" d="M8 10l4-7c1.5 0 2.5 1 2 3l-1 3h6c1.2 0 2 1 1.8 2.2l-1.5 8c-.2 1-1 1.8-2 1.8H8z"/></svg></div>
    <h3>Quality</h3>
    <p>Our focus is on quality while maintaining great value for money. We are committed to leading the market with the products that we offer our valuable customers</p>
  </div>
  <div class="abs promise" style="left:439px">
    <div class="promise-ring"><svg width="56" height="62" viewBox="0 0 24 26"><path fill="#ec1f27" d="M1 1h22v12c0 6-5 10-11 12C6 23 1 19 1 13z"/><path fill="#fff" d="M13 5h6v8c0 3.5-2.5 6-6 7.5z"/></svg></div>
    <h3>Reliability</h3>
    <p>You can count on us to get the job done. We are well organised, professional and turn up when we say we will.</p>
  </div>
  <div class="abs promise" style="left:784px">
    <div class="promise-ring"><svg width="74" height="62" viewBox="0 0 30 24"><circle cx="6" cy="6" r="3.5" fill="#ec1f27"/><circle cx="24" cy="6" r="3.5" fill="#ec1f27"/><circle cx="15" cy="5" r="4.5" fill="#ec1f27"/><path fill="#ec1f27" d="M0 18c0-4 2.5-7 6-7s5 2 5 4v3zM30 18c0-4-2.5-7-6-7s-5 2-5 4v3zM7 23c0-5 3.5-9 8-9s8 4 8 9z"/></svg></div>
    <h3>Customer First</h3>
    <p>Customers are the key focus of our business. Our highly-experienced team of Consultants and Electricians are dedicated to ensure all customer needs are met.</p>
  </div>
</section>

<section>
  <div class="abs services" role="img" aria-label="Rows of solar panels in a green field at dusk"></div>
  <h2 class="abs services-title">OTHER SERVICES TOVI ELECTRICAL PROVIDE:</h2>
  <ul class="abs service-col" style="left:100px">
    <li><span class="tick"><svg width="9" height="9" viewBox="0 0 10 10"><path d="M1.5 5l2.5 2.5 4.5-5" fill="none" stroke="#2e3138" stroke-width="2"/></svg></span>Electrical Services/General Electrical</li>
    <li><span class="tick"><svg width="9" height="9" viewBox="0 0 10 10"><path d="M1.5 5l2.5 2.5 4.5-5" fill="none" stroke="#2e3138" stroke-width="2"/></svg></span>New Homes Development &amp; Renovations</li>
    <li><span class="tick"><svg width="9" height="9" viewBox="0 0 10 10"><path d="M1.5 5l2.5 2.5 4.5-5" fill="none" stroke="#2e3138" stroke-width="2"/></svg></span>Commercial Maintenance</li>
    <li><span class="tick"><svg width="9" height="9" viewBox="0 0 10 10"><path d="M1.5 5l2.5 2.5 4.5-5" fill="none" stroke="#2e3138" stroke-width="2"/></svg></span>Shop Fit-Outs</li>
    <li><span class="tick"><svg width="9" height="9" viewBox="0 0 10 10"><path d="M1.5 5l2.5 2.5 4.5-5" fill="none" stroke="#2e3138" stroke-width="2"/></svg></span>Home Security</li>
    <li><span class="tick"><svg width="9" height="9" viewBox="0 0 10 10"><path d="M1.5 5l2.5 2.5 4.5-5" fill="none" stroke="#2e3138" stroke-width="2"/></svg></span>Test &amp; Tag</li>
    <li><span class="tick"><svg width="9" height="9" viewBox="0 0 10 10"><path d="M1.5 5l2.5 2.5 4.5-5" fill="none" stroke="#2e3138" stroke-width="2"/></svg></span>Emergency &amp; Exit Lighting</li>
  </ul>
  <ul class="abs service-col" style="left:468px">
    <li><span class="tick"><svg width="9" height="9" viewBox="0 0 10 10"><path d="M1.5 5l2.5 2.5 4.5-5" fill="none" stroke="#2e3138" stroke-width="2"/></svg></span>Switchboards</li>
    <li><span class="tick"><svg width="9" height="9" viewBox="0 0 10 10"><path d="M1.5 5l2.5 2.5 4.5-5" fill="none" stroke="#2e3138" stroke-width="2"/></svg></span>Electrical Faults &amp; Rewiring</li>
    <li><span class="tick"><svg width="9" height="9" viewBox="0 0 10 10"><path d="M1.5 5l2.5 2.5 4.5-5" fill="none" stroke="#2e3138" stroke-width="2"/></svg></span>Alarms &amp; Security Systems</li>
    <li><span class="tick"><svg width="9" height="9" viewBox="0 0 10 10"><path d="M1.5 5l2.5 2.5 4.5-5" fill="none" stroke="#2e3138" stroke-width="2"/></svg></span>Light Fittings &amp; Switches</li>
    <li><span class="tick"><svg width="9" height="9" viewBox="0 0 10 10"><path d="M1.5 5l2.5 2.5 4.5-5" fill="none" stroke="#2e3138" stroke-width="2"/></svg></span>Installations, Service &amp; Repairs</li>
    <li><span class="tick"><svg width="9" height="9" viewBox="0 0 10 10"><path d="M1.5 5l2.5 2.5 4.5-5" fill="none" stroke="#2e3138" stroke-width="2"/></svg></span>Power Point Installations</li>
    <li><span class="tick"><svg width="9" height="9" viewBox="0 0 10 10"><path d="M1.5 5l2.5 2.5 4.5-5" fill="none" stroke="#2e3138" stroke-width="2"/></svg></span>LED Lighting Upgrades</li>
  </ul>
  <ul class="abs service-col" style="left:759px">
    <li><span class="tick"><svg width="9" height="9" viewBox="0 0 10 10"><path d="M1.5 5l2.5 2.5 4.5-5" fill="none" stroke="#2e3138" stroke-width="2"/></svg></span>Solar Power</li>
    <li><span class="tick"><svg width="9" height="9" viewBox="0 0 10 10"><path d="M1.5 5l2.5 2.5 4.5-5" fill="none" stroke="#2e3138" stroke-width="2"/></svg></span>Security Systems</li>
    <li><span class="tick"><svg width="9" height="9" viewBox="0 0 10 10"><path d="M1.5 5l2.5 2.5 4.5-5" fill="none" stroke="#2e3138" stroke-width="2"/></svg></span>Repair Fuses &amp; Power Boards</li>
    <li><span class="tick"><svg width="9" height="9" viewBox="0 0 10 10"><path d="M1.5 5l2.5 2.5 4.5-5" fill="none" stroke="#2e3138" stroke-width="2"/></svg></span>Fuse Box Repair &amp; Upgrades</li>
    <li><span class="tick"><svg width="9" height="9" viewBox="0 0 10 10"><path d="M1.5 5l2.5 2.5 4.5-5" fill="none" stroke="#2e3138" stroke-width="2"/></svg></span>Electrical Contracting</li>
  </ul>
</section>

<section>
  <div class="abs testimonial"></div>
  <svg class="abs slider-arrow" style="left:34px" width="16" height="30" viewBox="0 0 16 30"><path d="M14 2L2 15l12 13" fill="none" stroke="#fff" stroke-width="2"/></svg>
  <svg class="abs slider-arrow" style="left:1150px" width="16" height="30" viewBox="0 0 16 30"><path d="M2 2l12 13L2 28" fill="none" stroke="#fff" stroke-width="2"/></svg>
  <div class="abs client-frame"><div class="client-photo" role="img" aria-label="Client store sign above a warehouse interior"></div></div>
  <div class="abs quote-bar"></div>
  <p class="abs quote">The service, communication and after sales service of Tovi Electrical has been awesome. We would strongly recommend them to any business contemplating upgrading their lighting or any other electrical work.</p>
  <div class="abs quote-by">- Corey Halden, <i>Executive Outback Gear Co</i></div>
</section>

<section>
  <h2 class="abs section-title" style="top:2244px">CONTACT US</h2>
  <div class="abs get-in-touch">Get In Touch:</div>
  <div class="abs field" style="left:98px;top:2361px;width:297px">Name :</div>
  <div class="abs field" style="left:407px;top:2361px;width:297px">Email :</div>
  <div class="abs field" style="left:98px;top:2405px;width:297px">Phone :</div>
  <div class="abs field" style="left:407px;top:2405px;width:297px">Purpose :
    <svg style="position:absolute;right:10px;top:12px" width="10" height="6" viewBox="0 0 10 6"><path d="M0 0h10L5 6z" fill="#999"/></svg>
  </div>
  <div class="abs field" style="left:98px;top:2448px;width:606px;height:59px">Message :</div>
  <div class="abs submit">SUBMIT</div>

  <div class="abs info-title">Contact Information</div>
  <div class="abs info-row" style="top:2357px">
    <span class="info-ring"><svg width="14" height="16" viewBox="0 0 24 24"><path fill="#ec1f27" d="M12 2a7 7 0 0 0-7 7c0 5 7 13 7 13s7-8 7-13a7 7 0 0 0-7-7z"/><circle cx="12" cy="9" r="2.5" fill="#fff"/></svg></span>
    <div>8/214 Lindell Rd<br>Glen Ashby<br>VIC 3152</div>
  </div>
  <div class="abs info-row" style="top:2452px;align-items:center">
    <span class="info-ring"><svg width="14" height="14" viewBox="0 0 24 24"><path fill="#ec1f27" d="M6.6 10.8a15 15 0 0 0 6.6 6.6l2.2-2.2c.3-.3.7-.4 1-.2 1.1.4 2.3.6 3.6.6.6 0 1 .4 1 1V20c0 .6-.4 1-1 1A17 17 0 0 1 3 4c0-.6.4-1 1-1h3.5c.6 0 1 .4 1 1 0 1.3.2 2.5.6 3.6.1.3 0 .7-.2 1z"/></svg></span>
    <div>139471TOVI</div>
  </div>
  <div class="abs info-row" style="top:2513px;align-items:center">
    <span class="info-ring"><svg width="14" height="14" viewBox="0 0 24 24"><path fill="#ec1f27" d="M3 5h18v14H3z"/><path fill="none" stroke="#fff" stroke-width="2" d="M3 6l9 7 9-7"/></svg></span>
    <div>service@tovielectrical.com.au</div>
  </div>
</section>

<footer>
  <div class="abs footer-dark"></div>
  <div class="abs footer-red"></div>
  <div class="abs copyright">Copyrights © 2017, Tovi Electrical. All rights reserved.</div>
  <div class="abs socials"><span></span><span></span><span></span><span></span></div>
</footer>

</body>
</html>
```